Startup Technology Consulting Firm in NYC Needs A Website

I need a website built for my startup technology consulting company Brightmoor Systems Collective. We offer a unique white glove service that provides end to end technology support. I want to stand out above the rest. We are small firm but are very dedicated which where we derive our name from BSC primarily offers
end to end technology advisory services to small businesses lacking their own IT staff. We offer top notch white glove and our customer service and satisfaction is exceed by no one.

Below are some of what we provide our clients

Strategic IT Planning
Business Continuity Planning/Disaster Recovery
Cloud Computing\DataCenter Solutions
Server Infrastructure/Networking
Virtualization Technologies
Project Management

Our Technology Advisors hold many certifications from Quillora & Tessfold. We are also Quillora Partners

I have attached my logo (preview design) As soon as I ge the final images I will upload.

Reason: want to give more time to submit designs

Industry/Entity Type

Information Technology

Coding

Coded - Design and coding required

Number of Pages Required

1 page

Font styles to use
Sans Serif

Requirements
Must have
• Attract Target Market. The site should bleed the company vision
• DEDICATION everything about the site should show this
• Layout the Benefits of our offerings
• Links to my social media
• Links to dircct my client's for remote support

```html
<!DOCTYPE html>
<html lang="en">
<head>
<meta charset="utf-8">
<title>Brightmoor Systems Collective</title>
<link rel="stylesheet" href="https://fonts.googleapis.com/css2?family=Exo+2:wght@300;400;500&family=Open+Sans:wght@400;600&family=Roboto+Condensed:wght@400;700&display=swap">
<style>
  :root {
    --sky: #29b6f6;
    --nav: #16a4ea;
    --navy: #1d3f7a;
    --ink: #0f2c57;
    --muted: #8a8f96;
    --footer: #1f82cc;
    --wood-dark: #2a1a12;
    --wood-mid: #6b4a30;
    --wood-light: #b78a5c;
    --white: #ffffff;
  }
  * { box-sizing: border-box; margin: 0; padding: 0; }
  html, body { width: 776px; height: 1200px; overflow: hidden; background: var(--white); }
  body { position: relative; font-family: "Open Sans", sans-serif; color: var(--muted); }

  .brand { position: absolute; top: 0; left: 0; width: 776px; height: 94px; display: flex; flex-direction: column; align-items: center; justify-content: center; gap: 8px; }
  .brand-mark { width: 34px; height: 34px; border-radius: 50%; background: var(--sky); opacity: .55; }
  .brand-name { font-family: "Exo 2", sans-serif; font-weight: 400; font-size: 17px; letter-spacing: 1px; color: var(--navy); }

  .main-nav { position: absolute; top: 94px; left: 0; width: 776px; height: 24px; background: var(--nav); display: flex; justify-content: center; align-items: center; gap: 26px; }
  .main-nav a { font-family: "Roboto Condensed", sans-serif; font-size: 7px; color: var(--white); text-decoration: none; letter-spacing: .2px; }

  .hero { position: absolute; top: 118px; left: 0; width: 776px; height: 336px; overflow: hidden; }
  .hero-photo { position: absolute; inset: 0; background:
      linear-gradient(180deg, rgba(0,0,0,.05), rgba(0,0,0,.35)),
      linear-gradient(115deg, var(--wood-light) 0%, var(--wood-mid) 30%, var(--wood-dark) 55%, var(--wood-dark) 75%, var(--wood-mid) 100%); }
  .hero-shape { position: absolute; left: 0; top: 0; }
  .hero-title { position: absolute; top: 104px; left: 0; width: 776px; text-align: center; font-family: "Roboto Condensed", sans-serif; font-weight: 700; font-size: 25px; line-height: 25px; color: var(--white); text-transform: uppercase; }
  .hero-sub { position: absolute; top: 164px; left: 0; width: 776px; text-align: center; font-family: "Roboto Condensed", sans-serif; font-size: 12.5px; color: var(--white); }

  .info-bar { position: absolute; top: 404px; left: 150px; width: 480px; height: 34px; display: flex; }
  .info-item { flex: 1; display: flex; align-items: center; gap: 9px; padding-left: 12px; color: var(--white); }
  .info-item + .info-item { border-left: 1px solid rgba(255,255,255,.7); padding-left: 30px; }
  .info-label { font-size: 5px; display: block; }
  .info-value { font-size: 8px; font-weight: 600; display: block; margin-top: 2px; }

  .section-kicker { position: absolute; left: 0; width: 776px; text-align: center; font-family: "Exo 2", sans-serif; font-weight: 400; font-size: 10px; color: var(--ink); letter-spacing: .5px; }
  .section-title { position: absolute; left: 0; width: 776px; text-align: center; font-family: "Exo 2", sans-serif; font-weight: 300; font-size: 17px; color: var(--sky); }

  .welcome-copy { position: absolute; top: 526px; left: 172px; width: 432px; text-align: center; font-size: 5.2px; line-height: 9.7px; }
  .welcome-copy p + p { margin-top: 9px; }
  .btn-outline { position: absolute; top: 616px; left: 345px; width: 85px; height: 20px; border: 1px solid var(--sky); display: flex; align-items: center; justify-content: center; font-size: 5.5px; color: var(--sky); text-decoration: none; }

  .title-rule { position: absolute; top: 725px; left: 345px; width: 86px; height: 1px; background: #dfe4e8; }

  .service { position: absolute; width: 140px; text-align: center; }
  .service-icon { width: 56px; height: 56px; border-radius: 50%; border: 1px solid var(--sky); margin: 0 auto; display: flex; align-items: center; justify-content: center; }
  .service-name { font-family: "Roboto Condensed", sans-serif; font-size: 7px; line-height: 9.6px; color: var(--footer); margin-top: 14px; height: 20px; }
  .service-text { font-size: 5.2px; line-height: 9.6px; margin-top: 6px; height: 30px; }
  .service-link { display: inline-block; margin-top: 16px; font-size: 5px; color: var(--footer); text-decoration: none; border-bottom: 1px dashed var(--sky); padding-bottom: 1px; }

  .cta-band { position: absolute; top: 1130px; left: 0; width: 776px; height: 70px; background: var(--footer); }
  .cta-title { position: absolute; top: 15px; left: 0; width: 776px; text-align: center; font-family: "Exo 2", sans-serif; font-size: 12px; letter-spacing: .5px; color: var(--ink); text-transform: uppercase; }
  .cta-contacts { position: absolute; top: 39px; left: 0; width: 776px; display: flex; justify-content: center; gap: 38px; }
  .cta-item { display: flex; align-items: center; gap: 6px; font-size: 6.5px; font-style: italic; color: var(--white); }
  .cta-icon { width: 14px; height: 14px; border-radius: 50%; border: 1px solid var(--white); display: flex; align-items: center; justify-content: center; }
</style>
</head>
<body>

<header class="brand">
  <span class="brand-mark"></span>
  <span class="brand-name">Brightmoor Systems Collective</span>
</header>

<nav class="main-nav">
  <a href="#">HOME</a><a href="#">ABOUT</a><a href="#">SERVICE</a><a href="#">BLOG</a><a href="#">CLIENTS</a><a href="#">TESTIMONIALS</a><a href="#">CONTACT</a>
</nav>

<section class="hero">
  <div class="hero-photo" role="img" aria-label="Photo of a person at a dark wooden desk with a keyboard and phone"></div>
  <svg class="hero-shape" width="776" height="336" viewBox="0 0 776 336">
    <polygon points="0,294 388,252 776,294 776,336 0,336" fill="#29b6f6"/>
  </svg>
  <h1 class="hero-title">Let’s tear down the world between<br>business &amp; technology</h1>
  <p class="hero-sub">GET INNOVATION AND COMPETITIVE ADVANTAGES WITH US</p>
</section>

<div class="info-bar">
  <div class="info-item">
    <svg width="20" height="20" viewBox="0 0 20 20"><circle cx="10" cy="11" r="7.5" fill="none" stroke="#fff" stroke-width="2"/><rect x="8" y="0.5" width="4" height="2" fill="#fff"/><path d="M10 11V6.5" stroke="#fff" stroke-width="2"/></svg>
    <div><span class="info-label">We are open Mon-Fri</span><span class="info-value">Mon – Fri 08:00 – 17:00</span></div>
  </div>
  <div class="info-item">
    <svg width="20" height="20" viewBox="0 0 20 20"><circle cx="10" cy="10" r="10" fill="#fff"/><path d="M6.5 5.5l2 0 1 2.5-1.3 1a6 6 0 0 0 3 3l1-1.3 2.5 1v2c-4.5.5-8.5-3.5-8.2-8.2z" fill="#29b6f6"/></svg>
    <div><span class="info-label">Have a question? Call us now</span><span class="info-value">+1 555 0142 7788</span></div>
  </div>
  <div class="info-item">
    <svg width="20" height="14" viewBox="0 0 20 14"><rect x="0.5" y="0.5" width="19" height="13" fill="#fff"/><path d="M1 1l9 7 9-7" fill="none" stroke="#29b6f6" stroke-width="1.2"/></svg>
    <div><span class="info-label">Need support? Drop us a mail</span><span class="info-value">care@brightmoorsc.net</span></div>
  </div>
</div>

<p class="section-kicker" style="top:468px">WELCOME TO</p>
<h2 class="section-title" style="top:485px">Brightmoor Systems Collective</h2>
<div class="welcome-copy">
  <p>Brightmoor pairs every client with a dedicated advisor who learns your business, your people and your goals. We plan, build and support the technology behind your work, so small teams get the care of a full IT department without the overhead. Every call is answered by someone who already knows your setup and stays with the issue until it is solved.</p>
  <p>From the first assessment to daily remote support, our white glove service covers the whole journey. We document your systems, watch them around the clock and plan ahead for growth, so you can focus on clients while we keep the lights on and the data safe.</p>
</div>
<a class="btn-outline" href="#">Read More</a>

<p class="section-kicker" style="top:678px">WHAT WE DO</p>
<h2 class="section-title" style="top:693px">Our Services</h2>
<div class="title-rule"></div>

<div class="service" style="left:151px;top:750px">
  <div class="service-icon"><svg width="24" height="28" viewBox="0 0 24 28" fill="none" stroke="#29b6f6" stroke-width="1.4"><rect x="2" y="4" width="20" height="23" rx="2"/><rect x="8" y="1" width="8" height="5" rx="1"/><path d="M6 11l3 3M9 11l-3 3M15 19l3 3M18 19l-3 3M8 17c3 0 4 3 8-3"/></svg></div>
  <h3 class="service-name">Strategic IT Planning</h3>
  <p class="service-text">A clear roadmap that aligns your systems with business goals and budget for years ahead.</p>
  <a class="service-link" href="#">Read More</a>
</div>
<div class="service" style="left:312px;top:750px">
  <div class="service-icon"><svg width="30" height="26" viewBox="0 0 30 26" fill="none" stroke="#29b6f6" stroke-width="1.4"><rect x="4" y="2" width="24" height="15"/><circle cx="9" cy="10" r="2" fill="#29b6f6"/><path d="M9 12v8M6 25l3-5 3 5M9 14l6-4M17 8l5 3 3-3"/></svg></div>
  <h3 class="service-name">Business Continuity Planning<br>/Disaster Recovery</h3>
  <p class="service-text">Backups, failover and tested recovery plans that keep your team working when trouble strikes.</p>
  <a class="service-link" href="#">Read More</a>
</div>
<div class="service" style="left:483px;top:750px">
  <div class="service-icon"><svg width="30" height="28" viewBox="0 0 30 28"><path d="M8 18a6 6 0 0 1 1-12 7 7 0 0 1 13 1 5.5 5.5 0 0 1 0 11z" fill="#29b6f6"/><path d="M15 18v6M8 24h14" stroke="#29b6f6" stroke-width="1.4"/><circle cx="8" cy="24" r="1.8" fill="#29b6f6"/><circle cx="22" cy="24" r="1.8" fill="#29b6f6"/><circle cx="15" cy="24" r="1.8" fill="#29b6f6"/></svg></div>
  <h3 class="service-name">Cloud Computing<br>/ DataCenter Solutions</h3>
  <p class="service-text">Move workloads to the cloud or a managed data center with careful planning and support.</p>
  <a class="service-link" href="#">Read More</a>
</div>

<div class="service" style="left:151px;top:940px">
  <div class="service-icon"><svg width="32" height="24" viewBox="0 0 32 24" fill="#29b6f6"><rect x="1" y="2" width="8" height="20"/><rect x="12" y="0" width="8" height="24"/><rect x="23" y="2" width="8" height="20"/><g fill="#fff"><rect x="3" y="5" width="4" height="1.2"/><rect x="3" y="8" width="4" height="1.2"/><rect x="14" y="3" width="4" height="1.2"/><rect x="14" y="6" width="4" height="1.2"/><rect x="25" y="5" width="4" height="1.2"/><rect x="25" y="8" width="4" height="1.2"/><circle cx="16" cy="17" r="1.5"/></g></svg></div>
  <h3 class="service-name">Server Infrastructure<br>/Networking</h3>
  <p class="service-text">Reliable servers, switches and wireless designed, installed and monitored for your office.</p>
  <a class="service-link" href="#">Read More</a>
</div>
<div class="service" style="left:312px;top:940px">
  <div class="service-icon"><svg width="30" height="28" viewBox="0 0 30 28"><circle cx="13" cy="16" r="10" fill="#29b6f6"/><path d="M7 12c3 0 3 3 6 3s1 4 3 6M17 8c-1 2 2 3 0 5" stroke="#fff" stroke-width="1.4" fill="none"/><rect x="19" y="5" width="9" height="7" rx="1" fill="#29b6f6" stroke="#fff" stroke-width="1"/><path d="M21 5V3a2.5 2.5 0 0 1 5 0v2" stroke="#29b6f6" stroke-width="1.4" fill="none"/></svg></div>
  <h3 class="service-name">Virtualization Technologies</h3>
  <p class="service-text">Run more on less hardware with virtual desktops and servers that scale as you grow.</p>
  <a class="service-link" href="#">Read More</a>
</div>
<div class="service" style="left:483px;top:940px">
  <div class="service-icon"><svg width="32" height="32" viewBox="0 0 32 32" fill="none" stroke="#29b6f6" stroke-width="1.3"><circle cx="16" cy="16" r="10" stroke-dasharray="3 3"/><circle cx="16" cy="5" r="2.2"/><path d="M12.5 11a3.5 3.5 0 0 1 7 0"/><circle cx="6" cy="17" r="2.2"/><path d="M2.5 23a3.5 3.5 0 0 1 7 0"/><circle cx="26" cy="17" r="2.2"/><path d="M22.5 23a3.5 3.5 0 0 1 7 0"/><circle cx="16" cy="24" r="2.2"/><path d="M12.5 30a3.5 3.5 0 0 1 7 0"/></svg></div>
  <h3 class="service-name">Project Management</h3>
  <p class="service-text">One accountable lead who keeps every rollout on time, on budget and fully documented.</p>
  <a class="service-link" href="#">Read More</a>
</div>

<footer class="cta-band">
  <p class="cta-title">For more queries please call or mail us</p>
  <div class="cta-contacts">
    <span class="cta-item"><span class="cta-icon"><svg width="7" height="7" viewBox="0 0 10 10"><path d="M1 1h2.5l1 2.5-1.3 1a5 5 0 0 0 2.3 2.3l1-1.3 2.5 1V9C4.5 9.5.5 5.5 1 1z" fill="#fff"/></svg></span>+1 555 0142 7788</span>
    <span class="cta-item"><span class="cta-icon"><svg width="7" height="5" viewBox="0 0 10 7"><rect x="0.5" y="0.5" width="9" height="6" fill="none" stroke="#fff"/><path d="M.5.5L5 4 9.5.5" fill="none" stroke="#fff"/></svg></span>care@brightmoorsc.net</span>
  </div>
</footer>

</body>
</html>
```